Willowgate Cabinet Setup Service needs a new flyer design

Willowgate Cabinet is a mobile furniture assembly service, that assembles furniture for the customer at there home or business

We are looking for a new feel and look to the flyer that we display within furniture stores based in Perth Western Australia.
The design must stand out to the customers that will be buying flatpack furniture and may need help assembling there products, from a simple chair, to a complete office / home fit out.

Our customer target varys from 18year olds to pensioners, male and female, and disabled.

we already have a logo, but must incorperate the company slogan " You buy We build" and also the words" At a price you can afford".

looking forward to seeing something new and away from the normal dull rubish, want to set a new benchmark.

please feel free to look at my website for information www.willowgatecabinet.com.au or willowgatecabinet
on facebook.

Sorry have altered the brief a little.

Will also be looking for a new wrap design for the company vans in the very near future.

Target Market(s)

women, builders, contractors, etc, people that dislike building flatpack furniture and are in need of help.

Industry/Entity Type

Business

Requirements
Must have
• if possisble to incorperate the colour scheme.website, facebook site, and( prices start from $10)

Must have my regestered tradmark stamp/mark
Should not have
• not cheesy or tackey

```html
<!DOCTYPE html>
<html lang="en">
<head>
<meta charset="utf-8">
<title>Willowgate Cabinet Setup Service – Flyer</title>
<link rel="stylesheet" href="https://fonts.googleapis.com/css2?family=Arimo:ital,wght@0,400;0,700;1,400;1,700&family=Open+Sans:ital,wght@0,600;0,700;1,400;1,600&family=Roboto+Slab:wght@800&family=Dancing+Script:wght@600&display=swap">
<style>
  :root {
    --sand: #e8dbc0;
    --sand-light: #f1e8d6;
    --sand-square: #dccaa3;
    --ink: #4a4230;
    --ink-grey: #555350;
    --olive: #b9a333;
    --olive-dark: #9c8a24;
    --brown: #6b3f1a;
    --brown-deep: #3d2510;
    --white: #ffffff;
    --wood: #d49a52;
    --photo-grey: #c9c3b8;
  }
  * { box-sizing: border-box; margin: 0; padding: 0; }
  html, body { width: 927px; height: 1200px; overflow: hidden; }
  body {
    position: relative;
    background: linear-gradient(180deg, #dac49a 0%, var(--sand) 38%, var(--sand-light) 70%, var(--sand) 100%);
    font-family: "Arimo", Arial, sans-serif;
  }
  .bg-square { position: absolute; background: var(--sand-square); opacity: .45; }

  .header {
    position: absolute; left: 29px; top: 40px; width: 870px; height: 170px;
    background: var(--white);
    border-bottom: 7px solid #2b2520;
    box-shadow: 0 2px 6px rgba(0,0,0,.2);
  }
  .brand { position: absolute; left: 60px; top: 38px; }
  .brand-row { display: flex; align-items: center; gap: 12px; }
  .brand-mark { width: 42px; height: 42px; background: var(--brown); }
  .brand-name {
    font-weight: 700; font-size: 27px; line-height: 27px; color: var(--brown);
  }
  .brand-slogan { margin-top: 8px; font-weight: 700; font-size: 15px; color: #8f7f5c; padding-left: 54px; }
  .brand-price { font-weight: 700; font-size: 14px; color: #8f7f5c; padding-left: 54px; margin-top: 2px; }

  .helper-photo {
    position: absolute; left: 450px; top: 16px; width: 230px; height: 142px;
    background: radial-gradient(ellipse at 60% 55%, #b9b6b0 0%, #e4e2de 55%, var(--white) 80%);
  }
  .need-help {
    position: absolute; left: 661px; top: 76px;
    font-family: "Arimo", Arial, sans-serif; font-weight: 700; font-size: 29px; color: #6b5a3c;
  }

  .assemble-list {
    position: absolute; left: 146px; top: 226px; display: flex; gap: 24px;
    font-weight: 700; font-size: 16px; color: var(--white);
    text-shadow: 0 0 2px #5a4a30, 1px 1px 2px #5a4a30;
  }
  .and-more {
    position: absolute; left: 675px; top: 245px;
    font-family: "Dancing Script", cursive; font-size: 13px; color: var(--white);
    text-shadow: 0 0 2px #5a4a30;
  }
  .service-title {
    position: absolute; left: 270px; top: 248px;
    font-family: "Roboto Slab", Georgia, serif; font-weight: 800; font-size: 26px; color: var(--white);
    text-shadow: -1px -1px 0 #4a3b24, 1px -1px 0 #4a3b24, -1px 1px 0 #4a3b24, 2px 2px 2px #4a3b24;
  }

  .photo { position: absolute; box-shadow: 0 3px 8px rgba(0,0,0,.35); border: 2px solid var(--white); }
  .photo-boxes { left: 32px; top: 348px; width: 100px; height: 118px; z-index: 1;
    background: linear-gradient(135deg, #b8956a, #d8c4a4); }
  .photo-parts { left: 130px; top: 326px; width: 134px; height: 164px; z-index: 2;
    background: linear-gradient(160deg, #dcd8d0 0%, #b59872 55%, #3a3a3a 100%); }
  .photo-main { left: 264px; top: 294px; width: 405px; height: 259px; z-index: 3;
    background: linear-gradient(160deg, #e8e4dc 0%, #d9b07a 45%, var(--wood) 70%, #cfc9c0 100%); }
  .photo-drill { left: 669px; top: 326px; width: 131px; height: 164px; z-index: 2;
    background: linear-gradient(135deg, #e0b07a 0%, #c8562e 55%, #3a3a3a 100%); }
  .photo-table { left: 800px; top: 348px; width: 94px; height: 118px; z-index: 1;
    background: linear-gradient(180deg, #a65a3e 0%, #c89a62 60%, #8a7a5e 100%); }

  .tagline { position: absolute; font-weight: 700; font-size: 23px; color: var(--ink); }
  .tagline-one { left: 200px; top: 562px; }
  .tagline-two { left: 432px; top: 600px; }
  .tagline em {
    font-style: normal; font-family: "Open Sans", sans-serif; font-weight: 700;
    font-size: 35px; color: var(--olive); text-shadow: 1px 1px 0 #6d5f1a;
  }

  .offer-panel {
    position: absolute; left: 29px; top: 658px; width: 872px; height: 518px;
    background: #efe5d2; box-shadow: 0 1px 5px rgba(0,0,0,.2);
  }
  .offer-card {
    position: absolute; left: 56px; top: 688px; width: 818px; height: 389px;
    background: var(--white); border: 1px solid #d9ccb0;
  }
  .price-fold {
    position: absolute; left: 172px; top: 674px; width: 0; height: 0;
    border-left: 14px solid transparent; border-bottom: 14px solid #2b2520;
  }
  .price-banner {
    position: absolute; left: 186px; top: 674px; width: 562px; height: 131px;
    background: var(--olive); box-shadow: 0 3px 4px rgba(0,0,0,.35);
    display: flex; align-items: center; padding-left: 40px;
    font-family: "Open Sans", sans-serif; color: var(--white);
  }
  .price-lead { font-weight: 600; font-size: 38px; letter-spacing: -.5px; text-shadow: 1px 1px 2px rgba(0,0,0,.4); }
  .price-amount {
    margin-left: 20px; font-weight: 700; font-size: 108px; letter-spacing: -6px; line-height: 1;
    text-shadow: 2px 3px 3px rgba(0,0,0,.45);
  }
  .offer-copy {
    position: absolute; left: 80px; top: 818px; width: 780px;
    font-weight: 700; font-size: 21.5px; line-height: 27px; color: var(--ink-grey);
  }
  .offer-copy p + p { margin-top: 20px; }

  .contact-bar {
    position: absolute; left: 56px; top: 1096px; width: 818px; height: 64px;
    background: var(--brown); border: 1px solid var(--brown-deep);
    color: var(--white); text-align: center; font-family: "Open Sans", sans-serif; font-style: italic;
  }
  .contact-heading { font-size: 19px; margin-top: 6px; }
  .contact-details { font-weight: 700; font-size: 15px; margin-top: 2px; display: flex; justify-content: center; gap: 16px; }
</style>
</head>
<body>
  <div class="bg-square" style="left:0;top:0;width:110px;height:70px"></div>
  <div class="bg-square" style="left:220px;top:10px;width:90px;height:60px"></div>
  <div class="bg-square" style="left:760px;top:0;width:120px;height:60px"></div>
  <div class="bg-square" style="left:110px;top:250px;width:60px;height:50px"></div>
  <div class="bg-square" style="left:740px;top:250px;width:90px;height:60px"></div>
  <div class="bg-square" style="left:840px;top:220px;width:70px;height:70px"></div>

  <header class="header">
    <div class="brand">
      <div class="brand-row">
        <div class="brand-mark"></div>
        <div class="brand-name">Willowgate<br>Cabinet</div>
      </div>
      <div class="brand-slogan">you buy we build</div>
      <div class="brand-price">At a price you can afford</div>
    </div>
    <div class="helper-photo" role="img" aria-label="Photo of a woman sitting on the floor assembling flat-pack furniture with a screwdriver"></div>
    <div class="need-help">need help?</div>
  </header>

  <div class="assemble-list"><span>WE ASSEMBLE:&nbsp; COMPUTERDESKS</span><span>BEDROOM FURNITURE</span><span>KITCHEN</span></div>
  <div class="and-more">...and more</div>
  <h1 class="service-title">Furniture assembly service</h1>

  <div class="photo photo-boxes" role="img" aria-label="Photo of flat-pack cardboard boxes leaning against a wall"></div>
  <div class="photo photo-parts" role="img" aria-label="Photo of bagged screws and fittings on a board"></div>
  <div class="photo photo-main" role="img" aria-label="Photo of a man kneeling among pine panels reading assembly instructions"></div>
  <div class="photo photo-drill" role="img" aria-label="Photo of a cordless drill on pine timber"></div>
  <div class="photo photo-table" role="img" aria-label="Photo of an assembled timber table and chairs on a patio"></div>

  <p class="tagline tagline-one">We take the <em>frustration</em></p>
  <p class="tagline tagline-two">out of <em>furniture</em> assembly!</p>

  <section class="offer-panel"></section>
  <div class="offer-card"></div>
  <div class="price-fold"></div>
  <div class="price-banner">
    <span class="price-lead">Prices start from</span>
    <span class="price-amount">$10</span>
  </div>
  <div class="offer-copy">
    <p>Why spend your day struggling with the assembly of your new flat-pack furniture, when one of our skilled technicians can have your furniture assembled and installed in no time, without the hassel of having to assemble the items yourself.</p>
    <p>We will always work around your schedule, with one of our experienced technicians available when you need them. Willowgate Cabinet is a furniture assembly service that takes the frustration out furniture assembly, at an affordable price.</p>
  </div>

  <footer class="contact-bar">
    <div class="contact-heading">For more information please contact:</div>
    <div class="contact-details">
      <span>Tel: 0491570156</span>
      <span>Email: info@willowgatecabinet.com.au</span>
      <span>Web: www.willowgatecabinet.com.au</span>
    </div>
  </footer>
</body>
</html>
```